Volunteer Fire Department Website Refresh

I need a redesign of a website, www.tbnhq.org, I built for a volunteer fire department several years ago. I plan to reuse the existing content except for the stock photos on the landing page. I would like the website to be responsive and mobile friendly, using bootstrap 4 and the use of Material Design is optional. Overall I would like to stick with a darker color scheme with dark gray, red, and yellow similar to this template https://www.layoutquarry.com/demo/51937.html
Fire Department
Coded - Design and coding required
5+ page

```html
<!DOCTYPE html>
<html lang="en">
<head>
<meta charset="utf-8">
<title>Tilbury Bend Volunteer Fire Department</title>
<link href="https://fonts.googleapis.com/css2?family=Oswald:wght@400;500;600;700&family=Open+Sans:wght@400;600;700&display=swap" rel="stylesheet">
<style>
:root{
  --red:#c4140f;
  --red-dark:#8e0c08;
  --yellow:#f4a21a;
  --gold:#e8a020;
  --ink:#1c1c1c;
  --panel:#232323;
  --panel-2:#2b2b2b;
  --black:#0e0e0e;
  --text:#bdbdbd;
  --white:#ffffff;
}
*{box-sizing:border-box;margin:0;padding:0}
html,body{width:1200px;height:2552px;overflow:hidden;background:var(--black)}
body{font-family:"Open Sans",Arial,sans-serif;color:var(--text);font-size:14px;line-height:1.7}
h1,h2,h3,.nav a,.btn{font-family:"Oswald",Arial,sans-serif;text-transform:uppercase}

/* Hero */
.hero{position:relative;height:600px;background:linear-gradient(100deg,#1a1411 0%,#3b2417 40%,#a2491c 70%,#e7902f 100%);overflow:hidden}
.hero-photo{position:absolute;inset:0;background:radial-gradient(ellipse at 72% 60%,rgba(255,190,80,.55),rgba(0,0,0,0) 55%),linear-gradient(180deg,rgba(0,0,0,.35),rgba(0,0,0,.15) 40%,rgba(0,0,0,.55))}
.topbar{position:absolute;top:0;left:0;right:0;height:120px;display:flex;align-items:center;padding:0 100px 0 110px}
.brand{display:flex;align-items:center;gap:14px;color:var(--white);font-family:"Oswald",sans-serif;font-weight:600;font-size:20px;letter-spacing:1px}
.brand-mark{width:80px;height:80px;border-radius:50%;background:#2a2a2a;border:3px solid var(--gold)}
.nav{margin-left:auto;display:flex;align-items:center;gap:30px}
.nav a{color:var(--white);text-decoration:none;font-size:15px;letter-spacing:1px;font-weight:500}
.nav a.active{color:var(--yellow)}
.social{width:38px;height:38px;border-radius:50%;background:var(--white)}
.btn{display:inline-block;font-size:14px;letter-spacing:1px;padding:8px 22px;border-radius:20px;text-decoration:none;font-weight:500}
.btn-yellow{background:var(--yellow);color:var(--white)}
.btn-outline{border:2px solid #8a8a8a;color:var(--white)}
.hero-title{position:absolute;left:110px;top:330px}
.hero-title .small{display:block;color:var(--white);font-size:58px;font-weight:500;line-height:1.1}
.hero-title .big{display:block;color:var(--red);font-size:92px;font-weight:700;line-height:1}
.dots{position:absolute;bottom:28px;left:0;right:0;display:flex;justify-content:center;gap:10px}
.dots span{width:10px;height:10px;border-radius:50%;background:rgba(255,255,255,.45)}
.dots span.on{background:var(--white)}

/* Welcome */
.welcome{height:480px;background:var(--panel);padding:50px 100px 0;display:flex;gap:40px}
.welcome-text{flex:1}
.welcome h2{color:var(--white);font-size:26px;font-weight:600;margin-bottom:14px}
.welcome h2 span{color:var(--yellow)}
.welcome p{font-size:13.5px;margin-bottom:12px}
.welcome .btn{margin-top:10px}
.roster{width:310px;background:var(--red);align-self:flex-start;margin-top:2px}
.roster h3{background:var(--red-dark);color:var(--yellow);font-size:18px;text-align:center;padding:10px 0;font-weight:600}
.roster table{width:100%;border-collapse:collapse;font-size:13px;color:var(--white)}
.roster th{text-align:left;padding:8px 16px;font-family:"Oswald",sans-serif;font-weight:500;color:var(--yellow);border-bottom:1px solid rgba(255,255,255,.25)}
.roster td{padding:5px 16px;border-bottom:1px solid rgba(255,255,255,.15)}
.roster td:last-child,.roster th:last-child{text-align:right}

/* Features */
.features{height:540px;background:var(--ink);padding:60px 100px 0;display:flex;gap:30px}
.feature{flex:1}
.feature h3{background:var(--red);color:var(--white);font-size:20px;font-weight:500;padding:8px 16px;letter-spacing:1px}
.feature-photo{height:160px;margin:10px 0 36px}
.feature p{font-size:13px;height:112px}
.feature .btn{margin-top:28px;font-size:13px;padding:6px 20px}

/* Gallery */
.gallery{height:560px;background:var(--panel-2);padding:70px 100px 0}
.gallery-head{display:flex;align-items:center;justify-content:space-between;margin-bottom:26px}
.gallery h2{color:var(--white);font-size:32px;font-weight:500}
.gallery h2 span{color:var(--yellow)}
.grid{display:grid;grid-template-columns:repeat(5,1fr);gap:20px}
.grid div{height:136px}

/* Footer */
.footer{height:312px;background:var(--black);padding:40px 100px 0;display:flex;gap:50px}
.footer-brand{width:150px;display:flex;flex-direction:column;align-items:center;gap:10px;color:var(--white);font-family:"Oswald",sans-serif;font-size:16px;font-weight:600}
.footer-brand .brand-mark{width:110px;height:110px}
.footer h4{font-family:"Oswald",sans-serif;color:var(--white);font-size:16px;font-weight:500;margin-bottom:14px}
.contact{width:240px}
.contact li{list-style:none;display:flex;align-items:center;gap:12px;font-size:12.5px;margin-bottom:14px}
.contact .ic{width:26px;height:26px;border-radius:50%;background:var(--red);display:flex;align-items:center;justify-content:center;flex:none}
.menu{width:170px}
.menu li{list-style:none;font-size:12.5px;line-height:1.6}
.map{width:350px;height:200px;margin-left:auto;margin-top:0}
.copyright{height:40px;background:#050505;text-align:center;font-size:11px;line-height:40px;color:#8a8a8a}
</style>
</head>
<body>

<header class="hero">
  <div class="hero-photo" role="img" aria-label="Firefighters spraying a hose at a blazing fire"></div>
  <div class="topbar">
    <div class="brand"><span class="brand-mark"></span>TILBURY BEND</div>
    <nav class="nav">
      <a class="active" href="#">Home</a>
      <a href="#">History</a>
      <a href="#">Equipment</a>
      <a href="#">Members</a>
      <a href="#">Gallery</a>
      <a href="#">Alarms</a>
      <a href="#">Training</a>
      <span class="social"></span>
      <a class="btn btn-yellow" href="#">Join Rescue</a>
    </nav>
  </div>
  <h1 class="hero-title"><span class="small">Tilbury Bend</span><span class="big">Fire Rescue!</span></h1>
  <div class="dots"><span class="on"></span><span></span><span></span></div>
</header>

<section class="welcome">
  <div class="welcome-text">
    <h2>Welcome to <span>Tilbury Bend Volunteer Fire Departments</span></h2>
    <p>Welcome to the website of the Tilbury Bend Volunteer Fire Department. Visitors can find information covering our members, equipment, training, alarms, how to join, and much more. The history section includes details of the rich history and growth of our department, as compiled from records kept over the last several decades.</p>
    <p>Visitors can also find information on our members, like their name, date joined, years of service, and occupation. We also have a list of our past Fire Chiefs and Fire Marshals, Honorary Firefighters, Rescues, and a Memorial honoring the fallen firefighters of our department. The results of the annual drill are also posted here.</p>
    <p>New to this year is the "Protection" page and we have a top ten list of crew attendance for all members, listing how often each one responded to calls during the year.</p>
    <a class="btn btn-yellow" href="#">Read More</a>
  </div>
  <aside class="roster">
    <h3>Top Firefighters 2018</h3>
    <table>
      <tr><th>Firefighter</th><th>Attendance</th></tr>
      <tr><td>Dale Hutton</td><td>92%</td></tr>
      <tr><td>Marco Lindell</td><td>88%</td></tr>
      <tr><td>Gavin Renner</td><td>80%</td></tr>
      <tr><td>Theo Marsh</td><td>74%</td></tr>
      <tr><td>Aaron Pryce</td><td>70%</td></tr>
      <tr><td>Wes Brandt</td><td>64%</td></tr>
      <tr><td>Ruben Calder</td><td>55%</td></tr>
      <tr><td>Lee Foster</td><td>50%</td></tr>
      <tr><td>Owen Sattler</td><td>47%</td></tr>
      <tr><td>Nick Ardley</td><td>41%</td></tr>
    </table>
  </aside>
</section>

<section class="features">
  <article class="feature">
    <h3>Equipment</h3>
    <div class="feature-photo" role="img" aria-label="Fire engines parked in the station garage" style="background:linear-gradient(135deg,#5a2620,#a8332a 55%,#d8c9b4)"></div>
    <p>The first piece of equipment purchased was a two-wheeled hose cart that could be pulled by firefighters. Soon after, a new pumper truck was purchased by the department.</p>
    <a class="btn btn-outline" href="#">Read More</a>
  </article>
  <article class="feature">
    <h3>Members</h3>
    <div class="feature-photo" role="img" aria-label="Group of department members in uniform before a rescue truck" style="background:linear-gradient(180deg,#6f1a16,#3c5a8c 55%,#20365c)"></div>
    <p>The department maintains an average membership of 30 firefighters, and currently has an active membership of 28. This membership has attended many meetings over the years.</p>
    <a class="btn btn-outline" href="#">Join Now</a>
  </article>
  <article class="feature">
    <h3>Training</h3>
    <div class="feature-photo" role="img" aria-label="Firefighter spraying water during a field training drill" style="background:linear-gradient(180deg,#9fc3e6,#dfe7ee 55%,#b9a58a)"></div>
    <p>The first piece of equipment purchased was a two-wheeled hose cart that could be pulled by firefighters. Soon after, a new pumper truck was purchased by the department.</p>
    <a class="btn btn-outline" href="#">Read More</a>
  </article>
</section>

<section class="gallery">
  <div class="gallery-head">
    <h2>Photo <span>Gallery</span></h2>
    <a class="btn btn-outline" href="#">View All</a>
  </div>
  <div class="grid">
    <div role="img" aria-label="Fire crew at a roadside scene" style="background:linear-gradient(160deg,#7a9ab8,#4a4a3a)"></div>
    <div role="img" aria-label="Department emblem on amber background" style="background:linear-gradient(160deg,#c98a1e,#6a4410)"></div>
    <div role="img" aria-label="Firefighters at a night fire" style="background:linear-gradient(160deg,#3a2a1e,#b0642a)"></div>
    <div role="img" aria-label="Fire truck in the field" style="background:linear-gradient(160deg,#a9c2da,#7a6a4e)"></div>
    <div role="img" aria-label="Red fire engines lined up" style="background:linear-gradient(160deg,#b3c6d6,#a8322a)"></div>
    <div role="img" aria-label="Crew outside the station" style="background:linear-gradient(160deg,#6c8a5e,#3a3a32)"></div>
    <div role="img" aria-label="Firefighters on a training ground" style="background:linear-gradient(160deg,#8aa0a8,#4e5a44)"></div>
    <div role="img" aria-label="Volunteers working with hoses" style="background:linear-gradient(160deg,#5e7050,#2c2c26)"></div>
    <div role="img" aria-label="Crew gathered around an engine" style="background:linear-gradient(160deg,#c6b8a0,#6a5a48)"></div>
    <div role="img" aria-label="Engine and tanker on a road" style="background:linear-gradient(160deg,#a4bccf,#8a4a3a)"></div>
  </div>
</section>

<footer>
  <div class="footer">
    <div class="footer-brand"><span class="brand-mark"></span>TILBURY BEND</div>
    <div class="contact">
      <h4>Contact Us</h4>
      <ul>
        <li><span class="ic"><svg width="12" height="14" viewBox="0 0 12 14"><path d="M6 0a5 5 0 0 0-5 5c0 4 5 9 5 9s5-5 5-9a5 5 0 0 0-5-5zm0 7a2 2 0 1 1 0-4 2 2 0 0 1 0 4z" fill="#fff"/></svg></span>214 Harlan Street,<br>Tilbury Bend</li>
        <li><span class="ic"><svg width="12" height="12" viewBox="0 0 12 12"><path d="M2.5 0l2 3-1.3 1.4a7 7 0 0 0 4.4 4.4L9 7.5l3 2-1.2 2.2C5 12 0 7 .3 1.2z" fill="#fff"/></svg></span>(555) 780-3400</li>
        <li><span class="ic"><svg width="13" height="10" viewBox="0 0 13 10"><rect x=".5" y=".5" width="12" height="9" fill="none" stroke="#fff"/><path d="M.5.5l6 5 6-5" fill="none" stroke="#fff"/></svg></span>info@tbnhq.org</li>
      </ul>
    </div>
    <div class="menu">
      <h4>Menu</h4>
      <ul>
        <li>Home</li><li>History</li><li>Equipment</li><li>Members</li><li>Gallery</li><li>Alarms</li><li>Training</li><li>Join Now</li><li>Contact Us</li>
      </ul>
    </div>
    <div class="map" role="img" aria-label="Street map showing the fire station location" style="background:linear-gradient(135deg,#e9e5dc,#d6dccf)"></div>
  </div>
  <div class="copyright">© Tilbury Bend Fire Dept. 2018 | All rights reserved</div>
</footer>

</body>
</html>
```